Business Card Design

Brantock Energy, L.P. is an energy and lifecycle management firm that creates value in petroleum products through synergistic marketing, trading, recovery, logistics and beneficial reuse services.

Sell top-quality refinery feedstock, petroleum products and co-products on the spot and futures makets (energy trading)

Separate, reclaim and/or manufacture valuable products for beneficial reuse (environmental)
Updates

The tag line Understanding Solutions   Performance are three different concepts and need to be kept either spaced apart or separated in some way. Thanks. 

Target Market(s)

Refiners, Petroleum storage companies, energy marketers

Industry/Entity Type

Business

Contact Information for Business Card

Glenda M. Holloway
Principal
Brantock Energy, L.P.
4817 Quimby St.
Houston, TX 77310
713-482-6159 phone
713-624-8841 fax
g.holloway@brantockenergy-example.com
www.brantockenergy-example.com

Requirements
Must have
• Tagline outlined in matching orange -

Understanding Solutions Performance
Nice to have
• Coordinating typestyles

```html
<!DOCTYPE html>
<html lang="en">
<head>
<meta charset="utf-8">
<title>Brantock Energy, L.P. — Business Card</title>
<link rel="stylesheet" href="https://fonts.googleapis.com/css2?family=Cinzel:wght@400;600;700&display=swap">
<style>
  :root {
    --backdrop: #8d8a84;
    --card-white: #ffffff;
    --card-silver: #d9d9d9;
    --ink: #1c1c1c;
    --ink-soft: #3a3a3a;
    --accent: #e8501e;
    --band: #141414;
    --band-text: #9a9a9a;
  }
  * { box-sizing: border-box; margin: 0; padding: 0; }
  html, body {
    width: 1200px; height: 871px; overflow: hidden;
    background: var(--backdrop);
    font-family: "Cinzel", serif;
  }
  .sheet {
    position: relative; width: 1200px; height: 871px;
    display: flex; align-items: center; justify-content: center; gap: 40px;
  }
  .card {
    position: relative; width: 540px; height: 309px; overflow: hidden;
    box-shadow: 0 10px 28px rgba(0,0,0,0.35);
  }
  /* Front: logo side */
  .card--front {
    background: linear-gradient(160deg, var(--card-white) 0%, #f0f0f0 45%, var(--card-silver) 100%);
    display: flex; align-items: center; justify-content: center;
  }
  .brand { display: flex; align-items: center; gap: 14px; }
  .brand__dot {
    width: 44px; height: 44px; border-radius: 50%; background: var(--accent);
  }
  .brand__name {
    color: var(--ink); font-weight: 700; text-transform: uppercase;
    line-height: 1.02; letter-spacing: 0.04em;
  }
  .card--front .brand__name { font-size: 30px; }
  /* Back: contact side */
  .card--back { background: var(--card-white); }
  .card__wave { position: absolute; left: 0; top: 0; width: 540px; height: 309px; }
  .contact { position: absolute; left: 36px; top: 40px; color: var(--ink-soft); }
  .contact__name {
    font-size: 13px; font-weight: 600; color: var(--ink);
    font-variant: small-caps; letter-spacing: 0.04em;
  }
  .contact__role {
    font-size: 9px; color: var(--accent); text-transform: uppercase;
    letter-spacing: 0.06em; margin-top: 2px;
  }
  .contact__list { list-style: none; margin-top: 22px; }
  .contact__item {
    position: relative; padding-left: 20px; font-size: 10px;
    line-height: 15px; font-variant: small-caps; letter-spacing: 0.03em;
  }
  .contact__icon { position: absolute; left: 0; top: 3px; width: 9px; height: 9px; }
  .card--back .brand { position: absolute; right: 34px; top: 72px; gap: 10px; }
  .card--back .brand__dot { width: 34px; height: 34px; }
  .card--back .brand__name { font-size: 20px; }
  .card__web {
    position: absolute; right: 30px; bottom: 20px;
    color: var(--band-text); font-size: 11px; letter-spacing: 0.1em; text-transform: uppercase;
  }
</style>
</head>
<body>
<main class="sheet">
  <section class="card card--front" aria-label="Card front">
    <div class="brand">
      <span class="brand__dot"></span>
      <span class="brand__name">Brantock<br>Energy L.P.</span>
    </div>
  </section>

  <section class="card card--back" aria-label="Card back">
    <svg class="card__wave" viewBox="0 0 540 309" aria-hidden="true">
      <path d="M0 176 C 120 196, 250 258, 360 238 C 430 226, 490 200, 540 196 L540 309 L0 309 Z" fill="var(--band)"/>
      <path d="M0 168 C 120 188, 250 250, 360 230 C 430 218, 490 192, 540 188 L540 196 C 490 200, 430 226, 360 238 C 250 258, 120 196, 0 176 Z" fill="#ffffff"/>
      <path d="M0 160 C 120 180, 250 242, 360 222 C 430 210, 490 184, 540 180 L540 186 C 490 190, 430 216, 360 228 C 250 248, 120 186, 0 166 Z" fill="var(--accent)"/>
    </svg>

    <div class="contact">
      <p class="contact__name">Glenda M. Holloway</p>
      <p class="contact__role">Principal</p>
      <ul class="contact__list">
        <li class="contact__item">
          <svg class="contact__icon" viewBox="0 0 10 10" aria-hidden="true"><path d="M5 0.5a3.2 3.2 0 0 1 3.2 3.2C8.2 6 5 9.5 5 9.5S1.8 6 1.8 3.7A3.2 3.2 0 0 1 5 0.5z" fill="none" stroke="var(--accent)" stroke-width="1.1"/><circle cx="5" cy="3.7" r="1" fill="var(--accent)"/></svg>
          Brantock Energy, L.P.
        </li>
        <li class="contact__item">4817 Quimby St. Houston, TX</li>
        <li class="contact__item">
          <svg class="contact__icon" viewBox="0 0 10 10" aria-hidden="true"><path d="M2 1h2l1 2.3-1.2 1A6 6 0 0 0 5.7 6.2l1-1.2L9 6v2a1 1 0 0 1-1 1A7.5 7.5 0 0 1 1 2a1 1 0 0 1 1-1z" fill="var(--accent)"/></svg>
          77310 713-482-6159 phone
        </li>
        <li class="contact__item">
          <svg class="contact__icon" viewBox="0 0 10 10" aria-hidden="true"><rect x="1" y="3.5" width="8" height="5" rx="0.8" fill="none" stroke="var(--accent)" stroke-width="1.1"/><rect x="3" y="1" width="4" height="3" fill="none" stroke="var(--accent)" stroke-width="1"/></svg>
          713-624-8841 fax
        </li>
        <li class="contact__item">
          <svg class="contact__icon" viewBox="0 0 10 10" aria-hidden="true"><rect x="0.8" y="2" width="8.4" height="6" fill="none" stroke="var(--accent)" stroke-width="1.1"/><path d="M0.8 2L5 5.5 9.2 2" fill="none" stroke="var(--accent)" stroke-width="1.1"/></svg>
          g.holloway@brantockenergy-example.com
        </li>
      </ul>
    </div>

    <div class="brand">
      <span class="brand__dot"></span>
      <span class="brand__name">Brantock<br>Energy L.P.</span>
    </div>

    <p class="card__web">www.brantockenergy-example.com</p>
  </section>
</main>
</body>
</html>
```